Interior design service, along with home organization, packing, and staging, home and business. As well as staging in conjunction with real estate sales.
Updates

Love many of your designs and will be choosing today. To inform you of the exact details needed, the name of the company is "Touches by Marla T" , my phone number and e-,ail need to be included. i also need either description or some sort of bullet points that give an idea of the following:

- Interior design for home and business
- Home organization and packing
- Staging for personal and professional space
- Real estate stagingĀ 

Thank you

Target Market(s)

wide audience, but most importantly people looking for a quality service

Industry/Entity Type

Real Estate

Contact Information for Business Card

Touches By Marla T
Marla Tovendi
(555)614-2937
mtbrook@mailnest.example

Requirements
Must have
• I'm 29 so i want my card to reflect something professional but still fresh. I don't have any specific photos or quotes that Ive included, however I like the card to reflect a personal touch, which is what I'm seeking from this service in the design of my card. Thanks!

```html
<!DOCTYPE html>
<html lang="en">
<head>
<meta charset="utf-8">
<title>Touches by Marla T – Business Card</title>
<link rel="stylesheet" href="https://fonts.googleapis.com/css2?family=Federo&family=Caveat:wght@500&family=Kalam:wght@700&display=swap">
<style>
  :root {
    --board: #e8dcc3;
    --board-deep: #dccdae;
    --card-blue: #8dcbd9;
    --card-green: #a2cf83;
    --band-green: #a6d488;
    --ink: #4a4748;
    --label-ink: #1e1b1a;
  }
  * { box-sizing: border-box; margin: 0; padding: 0; }
  html, body { width: 1200px; height: 900px; overflow: hidden; }
  body {
    position: relative;
    background: radial-gradient(ellipse at 40% 40%, var(--board) 0%, var(--board-deep) 100%);
    font-family: "Federo", sans-serif;
    color: var(--ink);
  }
  .side-label {
    position: absolute;
    font-family: "Kalam", cursive;
    font-size: 46px;
    color: var(--label-ink);
    line-height: 1;
  }
  .side-label--front { left: 262px; top: 60px; }
  .side-label--back { left: 852px; top: 452px; }

  .card {
    position: absolute;
    width: 583px;
    height: 333px;
    box-shadow: 3px 5px 8px rgba(0,0,0,0.45);
    overflow: hidden;
  }
  .card--front { left: 45px; top: 117px; }
  .card--back { left: 562px; top: 515px; }
  .card__bg { position: absolute; inset: 0; }

  .brand-name {
    position: absolute;
    left: 16px;
    font-family: "Federo", sans-serif;
    font-size: 40px;
    color: var(--ink);
    white-space: nowrap;
  }
  .card--front .brand-name { top: 40px; }
  .card--back .brand-name { top: 52px; font-size: 44px; }

  .service-band {
    position: absolute;
    left: 0;
    height: 34px;
    display: flex;
    align-items: center;
    justify-content: center;
    font-size: 19px;
    letter-spacing: 1px;
    color: var(--ink);
    box-shadow: 0 4px 5px rgba(0,0,0,0.25);
  }
  .card--front .service-band { top: 148px; width: 428px; }
  .card--back .service-band { top: 148px; width: 441px; }

  .script {
    position: absolute;
    font-family: "Caveat", cursive;
    font-weight: 500;
    color: var(--ink);
    white-space: nowrap;
  }
  .scope { left: 140px; top: 195px; font-size: 19px; }
  .owner { font-size: 40px; line-height: 1; }
  .owner--first { left: 425px; top: 170px; }
  .owner--last { left: 440px; top: 218px; }
  .contact { right: 12px; display: flex; align-items: center; gap: 8px; font-size: 20px; }
  .contact svg { fill: var(--ink); }
  .contact--phone { top: 266px; }
  .contact--email { top: 297px; }

  .services { left: 0; width: 441px; text-align: center; font-size: 21px; }
  .services--list { top: 190px; }
  .services--note { top: 225px; }
</style>
</head>
<body>
  <div class="side-label side-label--front">Front</div>
  <div class="side-label side-label--back">Back</div>

  <section class="card card--front">
    <svg class="card__bg" viewBox="0 0 583 333" width="583" height="333" aria-hidden="true">
      <rect width="583" height="333" fill="var(--card-blue)"/>
      <polygon points="467,0 583,0 583,333 405,333" fill="var(--card-green)"/>
      <rect y="148" width="428" height="34" fill="var(--band-green)"/>
    </svg>
    <div class="brand-name">Touches by Marla T</div>
    <div class="service-band">INTERIOR DESIGN SERVICE</div>
    <div class="script scope">HOME and BUSINESS</div>
    <div class="script owner owner--first">Marla</div>
    <div class="script owner owner--last">Tovendi</div>
    <div class="script contact contact--phone">
      <svg width="16" height="18" viewBox="0 0 24 24" aria-hidden="true"><path d="M6.6 10.8c1.4 2.8 3.8 5.1 6.6 6.6l2.2-2.2c.3-.3.7-.4 1-.2 1.1.4 2.3.6 3.6.6.6 0 1 .4 1 1V20c0 .6-.4 1-1 1C10.6 21 3 13.4 3 4c0-.6.4-1 1-1h3.5c.6 0 1 .4 1 1 0 1.3.2 2.5.6 3.6.1.3 0 .7-.2 1z"/></svg>
      (555)614-2937
    </div>
    <div class="script contact contact--email">
      <svg width="16" height="12" viewBox="0 0 16 12" aria-hidden="true"><path d="M0 0h16v1.5L8 7 0 1.5z"/><path d="M0 3.2l8 5.5 8-5.5V12H0z"/></svg>
      mtbrook@mailnest.example
    </div>
  </section>

  <section class="card card--back">
    <svg class="card__bg" viewBox="0 0 583 333" width="583" height="333" aria-hidden="true">
      <rect width="583" height="333" fill="var(--card-blue)"/>
      <polygon points="473,0 583,0 583,333 406,333" fill="var(--card-green)"/>
      <rect y="148" width="441" height="34" fill="var(--band-green)"/>
    </svg>
    <div class="brand-name">Touches by Marla T</div>
    <div class="service-band">INTERIOR DESIGN SERVICE</div>
    <div class="script services services--list">Home Organisation &nbsp;|&nbsp; Packing &nbsp;|&nbsp; Staging</div>
    <div class="script services services--note">Staging in conjuction with real estate sales</div>
  </section>
</body>
</html>
```